Real Estate Business Card

On the front side I want to have my info, my brokerage info.
On the back side I want have my complany’s logo, website and Facebook link. I will provide all this once I select a design.

I would like to see Black background and gold text, Dark Blue and gold text and White and blue text designs

Font styles to use
Sans Serif
Script

```html
<!DOCTYPE html>
<html lang="en">
<head>
<meta charset="utf-8">
<title>Crestline Realty – Business Card</title>
<link href="https://fonts.googleapis.com/css2?family=Lato:wght@400;700;900&display=swap" rel="stylesheet">
<style>
  :root {
    --backdrop: #353237;
    --card: #000000;
    --gold: #dcb54c;
    --gold-soft: #c9a043;
    --font-text: "Lato", sans-serif;
  }
  * { margin: 0; padding: 0; box-sizing: border-box; }
  html, body { width: 1200px; height: 462px; overflow: hidden; }
  body { background: var(--backdrop); font-family: var(--font-text); position: relative; }

  .card {
    position: absolute; top: 99px; width: 461px; height: 263px;
    background: var(--card); color: var(--gold);
  }
  .card--front { left: 139px; }
  .card--back { left: 634px; }

  .brand {
    position: absolute; text-align: center; transform: translate(-50%, -50%);
    display: flex; flex-direction: column; align-items: center; gap: 6px;
  }
  .brand__mark { width: 14px; height: 14px; background: var(--gold); }
  .brand__name { font-weight: 900; letter-spacing: 0.5px; white-space: nowrap; }
  .card--front .brand { left: 106px; top: 150px; }
  .card--front .brand__name { font-size: 26px; }
  .card--back .brand { left: 231px; top: 128px; gap: 10px; }
  .card--back .brand__mark { width: 22px; height: 22px; }
  .card--back .brand__name { font-size: 36px; }

  .divider {
    position: absolute; left: 223px; top: 44px; width: 2px; height: 175px;
    background: var(--gold-soft);
  }

  .contact { position: absolute; right: 86px; text-align: right; font-size: 9px; line-height: 11px; }
  .contact__name { top: 73px; font-size: 11px; font-weight: 700; }
  .contact__role { top: 87px; font-size: 6px; font-weight: 700; letter-spacing: 0.5px; }
  .contact__phone { top: 106px; font-weight: 700; }
  .contact__email { top: 138px; }
  .contact__address { top: 159px; }

  .icon { position: absolute; left: 384px; width: 16px; height: 16px; fill: none; stroke: var(--gold); stroke-width: 1.4; }
  .icon--phone { top: 111px; }
  .icon--mail { top: 137px; }
  .icon--pin { top: 160px; fill: var(--gold); stroke: none; }

  .link { position: absolute; right: 32px; font-size: 8.5px; font-weight: 700; line-height: 10px; }
  .link--web { top: 196px; }
  .link--social { top: 224px; }
  .badge {
    position: absolute; right: 0; width: 23px; height: 17px;
    background: var(--gold); border-radius: 3px 0 0 3px;
    display: flex; align-items: center; justify-content: center;
  }
  .badge--web { top: 192px; }
  .badge--social { top: 220px; }
  .badge svg { width: 11px; height: 11px; fill: none; stroke: #000; stroke-width: 1.3; }
  .badge__dot { width: 9px; height: 9px; border-radius: 50%; background: #000; }
</style>
</head>
<body>
  <section class="card card--front">
    <div class="brand">
      <span class="brand__mark"></span>
      <span class="brand__name">CRESTLINE</span>
    </div>
    <div class="divider"></div>

    <p class="contact contact__name">Dana Reyes</p>
    <p class="contact contact__role">BROKER</p>
    <p class="contact contact__phone">+41550123401<br>+41550123402</p>
    <p class="contact contact__email">dana.reyes@brokerhub.com</p>
    <p class="contact contact__address">Harbor Lane 8,<br>TOWN<br>5678 CA</p>

    <svg class="icon icon--phone" viewBox="0 0 16 16" aria-hidden="true">
      <path d="M3 2.5l2.5-.5 1.5 3-1.5 1.2c.8 1.8 2.2 3.2 4 4L10.7 8.7l3 1.5-.5 2.5c-.3.8-1.2 1.1-2 .9C6.7 12.4 3.6 9.3 2.4 4.8c-.2-.8.1-1.8.6-2.3z"/>
    </svg>
    <svg class="icon icon--mail" viewBox="0 0 16 16" aria-hidden="true">
      <rect x="1" y="3.5" width="14" height="9"/>
      <path d="M1 3.5l7 5.5 7-5.5M1 12.5l5-4.5M15 12.5l-5-4.5"/>
    </svg>
    <svg class="icon icon--pin" viewBox="0 0 16 16" aria-hidden="true">
      <path d="M8 1a5 5 0 0 0-5 5c0 3.6 5 9 5 9s5-5.4 5-9a5 5 0 0 0-5-5zm0 7.2A2.2 2.2 0 1 1 8 3.8a2.2 2.2 0 0 1 0 4.4z"/>
    </svg>
  </section>

  <section class="card card--back">
    <div class="brand">
      <span class="brand__mark"></span>
      <span class="brand__name">CRESTLINE</span>
    </div>

    <p class="link link--web">www.crestline.com</p>
    <div class="badge badge--web">
      <svg viewBox="0 0 12 12" aria-hidden="true">
        <circle cx="6" cy="6" r="5"/>
        <ellipse cx="6" cy="6" rx="2.2" ry="5"/>
        <path d="M1 6h10M2 3.3h8M2 8.7h8"/>
      </svg>
    </div>

    <p class="link link--social">social: @crestline</p>
    <div class="badge badge--social"><span class="badge__dot"></span></div>
  </section>
</body>
</html>
```